Business Cards

I'd like help creating business cards with the full logo "Veltrona Capital Partners" on the back of the card (navy background with white writing), and abbreviated logo "VCP" on the front. Would like to list name, title, phone number, email, and website listed on front of card. Would like to keep very simple. Front font Arial or similar.

```html
<!DOCTYPE html>
<html lang="en">
<head>
<meta charset="utf-8">
<title>Veltrona Capital Partners – Business Cards</title>
<link rel="stylesheet" href="https://fonts.googleapis.com/css2?family=Arimo:wght@400;700&display=swap">
<style>
  :root {
    --navy: #1c3f73;
    --white: #ffffff;
    --ink: #111111;
    --wave-grey: #b4b4b4;
    --backdrop: #4a4c50;
  }
  * { margin: 0; padding: 0; box-sizing: border-box; }
  html, body { width: 1200px; height: 887px; overflow: hidden; }
  body {
    background: var(--backdrop);
    font-family: "Arimo", Arial, sans-serif;
    position: relative;
  }
  .card {
    position: absolute;
    left: 290px;
    width: 620px;
    height: 354px;
    border-radius: 26px;
    overflow: hidden;
  }
  .card--back { top: 60px; background: var(--navy); }
  .card--front { top: 474px; background: var(--white); }

  .back-wordmark {
    position: absolute;
    inset: 0;
    display: flex;
    flex-direction: column;
    align-items: center;
    justify-content: center;
    color: var(--white);
    font-weight: 700;
    text-transform: uppercase;
    text-align: center;
  }
  .back-wordmark__name { font-size: 74px; letter-spacing: 2px; line-height: 1; }
  .back-wordmark__sub { font-size: 30px; letter-spacing: 11px; margin-top: 14px; line-height: 1; }

  .front-wave { position: absolute; inset: 0; width: 620px; height: 354px; }

  .front-monogram {
    position: absolute;
    left: 40px;
    top: 84px;
    width: 240px;
    text-align: center;
    color: var(--navy);
    font-weight: 700;
    font-size: 92px;
    letter-spacing: 2px;
    line-height: 1;
  }
  .front-divider {
    position: absolute;
    left: 300px;
    top: 48px;
    width: 2px;
    height: 146px;
    background: var(--navy);
  }
  .contact {
    position: absolute;
    left: 322px;
    top: 46px;
    color: var(--ink);
  }
  .contact__name {
    color: var(--navy);
    font-weight: 700;
    font-size: 24px;
    text-transform: uppercase;
    line-height: 1.1;
  }
  .contact__title { font-size: 17px; margin: 4px 0 12px; }
  .contact__list { list-style: none; }
  .contact__item {
    display: flex;
    align-items: center;
    gap: 9px;
    font-size: 17px;
    line-height: 1.45;
  }
  .contact__icon { width: 16px; height: 16px; flex: none; }
</style>
</head>
<body>

<section class="card card--back" aria-label="Card back">
  <div class="back-wordmark">
    <span class="back-wordmark__name">Veltrona</span>
    <span class="back-wordmark__sub">Capital Partners</span>
  </div>
</section>

<section class="card card--front" aria-label="Card front">
  <svg class="front-wave" viewBox="0 0 620 354" aria-hidden="true">
    <path d="M0,300 C170,330 320,310 420,262 C500,226 570,218 620,216 L620,354 L0,354 Z" fill="var(--navy)"/>
    <path d="M170,322 C320,312 380,276 450,242 C520,212 570,207 605,206" fill="none" stroke="var(--wave-grey)" stroke-width="5" stroke-linecap="round"/>
  </svg>

  <div class="front-monogram">VCP</div>
  <div class="front-divider"></div>

  <div class="contact">
    <p class="contact__name">Dara Whitcombe</p>
    <p class="contact__title">General Manager</p>
    <ul class="contact__list">
      <li class="contact__item">
        <svg class="contact__icon" viewBox="0 0 16 16" aria-hidden="true"><path d="M2 5c0-2 2-3 6-3s6 1 6 3l-3 1-1-2H6L5 6 2 5zM3 8h10v6H3z" fill="var(--navy)"/></svg>
        555-310-2846
      </li>
      <li class="contact__item">
        <svg class="contact__icon" viewBox="0 0 16 16" aria-hidden="true"><rect x="1" y="3" width="14" height="10" fill="var(--navy)"/><path d="M1 3l7 6 7-6" fill="none" stroke="var(--white)" stroke-width="1.4"/></svg>
        info@veltronacp.com
      </li>
      <li class="contact__item">
        <svg class="contact__icon" viewBox="0 0 16 16" aria-hidden="true"><circle cx="8" cy="8" r="7" fill="var(--navy)"/><path d="M1 8h14M8 1c-3 3-3 11 0 14M8 1c3 3 3 11 0 14" fill="none" stroke="var(--white)" stroke-width="1"/></svg>
        www.veltronacp.com
      </li>
    </ul>
  </div>
</section>

</body>
</html>
```